Rice importer and exporter. We need a new design for a 18 kg plastic bag.

We want to create a new brand of rice. This type of rice is produced in southeast Asia, imported to Portugal and sold to the local market. The target are people 30+ years old of all ethnicity. The name of the brand should be 'Kavrel', this is the name we want people to see and get used to it. <br/>Regarding the package itself. We want a simple bag, not with many different colours (3, 4 or 5) with preference to golden yellow. The Front page, should have our brand 'Kavrel' and the exact description of the type of rice 'Arroz 100% Jasmin Perfumado' and 'Premium Quality'. In the bag should also be included the nutrition facts, cooking instructions, a trasnparent part where customer can see the quality of the product and the our company info. Finally we would like to see in the front page the five stars and on the back the triple AAA (see examples of attached files). All the remaining should be of your imagination. <br/>Finally, the image 3 is an example of a bag structure that we want to make.

Target Market(s)

People 30+ years old

Font styles to use
Serif
Sans Serif

Colors
ffc214
fec214
fee18a
fbee3f
faef58
fbf289

Requirements
Must have
• 5 Stars on the front page, triple A's on the back and a transparent area for the customers to see the quality of the rice.

```html
<!DOCTYPE html>
<html lang="pt">
<head>
<meta charset="utf-8">
<title>Kavrel – Arroz 100% Jasmin Perfumado</title>
<link href="https://fonts.googleapis.com/css2?family=Encode+Sans+Semi+Condensed:wght@500;600;700&display=swap" rel="stylesheet">
<style>
  :root {
    --page-bg: #efe9e1;
    --gold-deep: #ffc214;
    --gold-light: #fee18a;
    --lemon: #faef58;
    --cream: #fbf289;
    --brand-orange: #e8590c;
    --ink: #111111;
    --rice-light: #f6f0e2;
    --rice-mid: #e7dcc3;
  }
  * { box-sizing: border-box; margin: 0; padding: 0; }
  html, body {
    width: 1200px; height: 800px; overflow: hidden;
    background: var(--page-bg);
    font-family: "Encode Sans Semi Condensed", "Arial Narrow", sans-serif;
  }
  .canvas { position: relative; width: 1200px; height: 800px; }
  .bag-front {
    position: absolute; left: 360px; top: 20px;
    width: 480px; height: 760px; overflow: hidden;
    background:
      linear-gradient(115deg, transparent 30%, rgba(255,194,20,.55) 45%, transparent 60%),
      linear-gradient(160deg, transparent 55%, rgba(248,150,20,.55) 80%, rgba(240,120,10,.7) 100%),
      linear-gradient(200deg, var(--gold-deep) 0%, var(--gold-light) 30%, var(--cream) 55%, var(--gold-deep) 100%);
  }
  .product-title {
    position: absolute; top: 136px; left: 0; width: 100%;
    text-align: center; color: var(--ink);
    font-size: 29px; font-weight: 700; letter-spacing: .2px;
  }
  .product-grade {
    position: absolute; top: 174px; left: 0; width: 100%;
    text-align: center; color: var(--ink);
    font-size: 19px; font-weight: 700;
  }
  .brand-name {
    position: absolute; top: 228px; left: 0; width: 100%;
    text-align: center; color: var(--brand-orange);
    font-size: 108px; font-weight: 700; line-height: 1;
  }
  .rating-stars { position: absolute; top: 368px; left: 167px; }
  .rice-window { position: absolute; left: 85px; top: 406px; }
  .company-info {
    position: absolute; left: 51px; top: 668px;
    font-size: 11.5px; font-weight: 600; color: var(--ink); line-height: 17.5px;
  }
  .net-weight {
    position: absolute; left: 310px; top: 666px; width: 134px;
    text-align: center; font-size: 20px; font-weight: 700; color: var(--ink); line-height: 26px;
  }
</style>
</head>
<body>
<div class="canvas">
  <section class="bag-front">
    <h1 class="product-title">Arroz 100% Jasmin Perfumado</h1>
    <p class="product-grade">Premium Quality</p>
    <p class="brand-name">Kavrel</p>

    <svg class="rating-stars" width="146" height="28" viewBox="0 0 146 28" aria-label="Cinco estrelas">
      <defs>
        <polygon id="star" points="13,1 16.5,9.5 25.5,10 18.5,15.8 20.8,24.8 13,19.8 5.2,24.8 7.5,15.8 0.5,10 9.5,9.5" fill="#e8590c"/>
      </defs>
      <use href="#star" x="0" y="2"/>
      <use href="#star" x="30" y="0"/>
      <use href="#star" x="60" y="0"/>
      <use href="#star" x="90" y="0"/>
      <use href="#star" x="120" y="2"/>
    </svg>

    <svg class="rice-window" width="320" height="230" viewBox="0 0 320 230">
      <defs>
        <radialGradient id="riceFill" cx="50%" cy="50%" r="60%">
          <stop offset="0%" stop-color="#f6f0e2"/>
          <stop offset="100%" stop-color="#e7dcc3"/>
        </radialGradient>
      </defs>
      <ellipse cx="160" cy="115" rx="155" ry="110" fill="url(#riceFill)" role="img" aria-label="Janela transparente com grãos de arroz jasmim e ilustração de dragão"/>
      <ellipse cx="160" cy="115" rx="155" ry="110" fill="none" stroke="#e8590c" stroke-width="7"/>
    </svg>

    <div class="company-info">
      <p>Telefone: 912 345 678</p>
      <p>Email: info@kavrelrice.pt</p>
      <p>Website: www.kavrelrice.pt</p>
    </div>
    <div class="net-weight">
      <p>Peso Liquido</p>
      <p>18kg</p>
    </div>
  </section>
</div>
</body>
</html>
```